Transformative School Model Needs a Website. I am easy to work with.

Greetings:
I am creating a K-12 school that is a complete and total re-imagination of what education can be for children, families, communities, and the planet. While we will begin as a K-12 school, I really see it as a complete life cycle education (birth to death). I'm looking for a website to describe my new transformational educational model. I anticipate having 7-8 pages. I have all the copy ready.
I am the Founder. I am easy to work with, an effective communicator, and I’m very good at knowing what I want and providing specific and concrete detail, examples, and direction to make sure I use your time wisely.

```html
<!DOCTYPE html>
<html lang="en">
<head>
<meta charset="utf-8">
<title>Serene Accord Academy</title>
<link href="https://fonts.googleapis.com/css2?family=Cinzel:wght@400;600&family=Roboto:ital,wght@0,400;0,500;0,700;1,400&display=swap" rel="stylesheet">
<style>
:root{
  --white:#ffffff;
  --ink:#111111;
  --body:#444444;
  --panel:#f4f4f4;
  --line:#d6d6d6;
  --gold:#ffc107;
  --flame:#ff5a0a;
  --orange:#ff8a00;
  --black:#000000;
}
*{margin:0;padding:0;box-sizing:border-box}
html,body{width:1200px;height:3617px;overflow:hidden}
body{position:relative;background:var(--white);font-family:'Roboto',Arial,sans-serif;color:var(--body)}
.abs{position:absolute}
.band{position:absolute;left:0;width:1200px}
.photo{position:absolute}
.heading{position:absolute;font-family:'Cinzel',Georgia,serif;font-weight:600;color:var(--ink);font-size:31px;line-height:30px;letter-spacing:1px}
.copy{position:absolute;font-size:11.6px;line-height:16.9px;color:var(--body)}
.btn{position:absolute;display:flex;align-items:center;justify-content:center;background:linear-gradient(90deg,var(--gold),var(--flame));color:var(--white);font-weight:700;font-size:13px;text-transform:uppercase}
.nav{position:absolute;left:0;width:1200px;display:flex;justify-content:center;font-size:13px;color:var(--white)}
.nav span{position:absolute;transform:translateX(-50%)}
.hero{top:0;height:554px;background:linear-gradient(180deg,#4d5660 0%,#5f6a70 30%,#8e9598 55%,#c9cccc 72%,#7a6a58 88%,#4a3f35 100%)}
.hero-line{top:58px;height:1px;background:rgba(255,255,255,.35)}
.hero-title{position:absolute;right:199px;top:205px;text-align:right;font-family:'Cinzel',Georgia,serif;font-weight:600;color:var(--white);font-size:46px;line-height:49px;letter-spacing:1px}
.seal{position:absolute;border:3px solid var(--white);border-radius:50%;display:flex;align-items:center;justify-content:center;text-align:center;font-family:'Cinzel',Georgia,serif;font-weight:600;color:var(--white)}
.testimonials{top:2705px;height:491px;background:linear-gradient(100deg,#ff5a0a 0%,#ff8a10 45%,#ffc414 100%)}
.quote{position:absolute;left:300px;width:600px;top:2966px;text-align:center;font-style:italic;font-size:14.5px;line-height:24.5px;color:var(--white)}
.dot{position:absolute;top:3129px;width:13px;height:13px;border:1.5px solid var(--white);border-radius:50%}
.field{position:absolute;top:3232px;height:40px;border:1px solid var(--line);background:var(--white);font-size:11.5px;color:#555;padding:14px 12px}
.footer{top:3308px;height:309px;background:var(--black)}
</style>
</head>
<body>

<!-- Hero -->
<section class="band hero" role="img" aria-label="Woman meditating on a rock above clouds with mountains behind"></section>
<div class="band hero-line"></div>
<nav class="nav" style="top:23px">
  <span style="left:239px">Home</span><span style="left:309px">About</span><span style="left:420px">School Foundations</span><span style="left:549px">Curriculum</span><span style="left:646px">Pedagogy</span><span style="left:744px">Outcomes</span><span style="left:837px">Opening</span><span style="left:940px">Testimonials</span>
</nav>
<div class="abs" style="left:220px;top:56px;width:36px;height:3px;background:linear-gradient(90deg,var(--gold),var(--flame))"></div>
<div class="seal" style="left:199px;top:195px;width:230px;height:230px;font-size:22px;line-height:30px">Serene<br>Accord<br>Academy</div>
<h1 class="hero-title">Serene<br>Accord<br>Academy</h1>
<div class="btn" style="left:881px;top:366px;width:117px;height:44px;font-size:15px">Read More</div>

<!-- Spiritual Philosophy -->
<div class="photo" role="img" aria-label="Hiker standing on a rock at golden sunset over hills" style="left:175px;top:620px;width:413px;height:369px;background:linear-gradient(180deg,#d9a63a 0%,#e7b236 40%,#b8781a 75%,#4a2e12 100%)"></div>
<h2 class="heading" style="left:641px;top:634px">Spiritual<br>Philosophy</h2>
<p class="copy" style="left:642px;top:708px;width:360px">The Planet is calling upon our consciousness to shift. While there is much to celebrate in the beauty and love that resides on Planet Earth, there is some tending to do. The water, soil, and air are sick. Animals—including men, women, boys, and girls—find themselves living in inhospitable and sometimes violent environments. So, tending we must. Education and Evolution are inextricably linked. Wisdom always serves to guide us (with courage) forward into unknown and new—yet promising—territory. Our strength will persevere and grow. With joy and grace, we'll do the work of restoring and rebuilding the planet such that life sustains and thrives. Serene Accord Academy is starting a school to do just that.</p>
<div class="btn" style="left:644px;top:925px;width:105px;height:38px">Read More</div>

<!-- Founder -->
<section class="band" style="top:1057px;height:521px;background:var(--panel)"></section>
<h2 class="heading" style="left:198px;top:1183px">Founder</h2>
<p class="copy" style="left:198px;top:1234px;width:352px">Lorem ipsum dolor sit amet, consectetur adipiscing elit, sed do eiusmod tempor incididunt ut labore et dolore magna aliqua. Quis ipsum suspendisse ultrices gravida. Risus commodo vivloreerra maecenas accumsan lacus vel facilisis. Lorem ipsum dolor lorsit amet, consectetur adipiscing elit, sed do eiusmod tempor incidunt ut labore et dolore magna aliqua. Quis ipsum suspendisse ultrices gravida. Risus commodo viverra maecenas accumsan lacus vel facilisis. Lorem ipsum dolor sit amet, consectetur adipiscing elit, sed do eiusmod tempor incididunt ut labore et dolore magna aliqu Quis ipsum suspendisse ultrices gravida.</p>
<div class="btn" style="left:198px;top:1423px;width:108px;height:39px">Read More</div>
<div class="photo" role="img" aria-label="Portrait of the smiling founder with long auburn hair" style="left:609px;top:1130px;width:411px;height:369px;background:linear-gradient(135deg,#cfc7bd 0%,#b49080 45%,#7a4a32 70%,#5e5a3e 100%)"></div>

<!-- Purpose -->
<div class="photo" role="img" aria-label="Woman seated in tall grass raising her arms toward the setting sun" style="left:175px;top:1653px;width:413px;height:369px;background:linear-gradient(180deg,#d7c9bd 0%,#e8b98a 40%,#8a7650 70%,#4f4a33 100%)"></div>
<h2 class="heading" style="left:643px;top:1753px">Purpose</h2>
<p class="copy" style="left:643px;top:1802px;width:370px;font-size:16.5px;line-height:22px">We design for wo/mankind to flourish, participate in public life, and live in harmony with the planet through aligning their souls, minds, and bodies to their hearts and collective imagination.</p>
<div class="btn" style="left:644px;top:1912px;width:110px;height:39px">Read More</div>

<!-- Statement of Oneness -->
<section class="band" style="top:2122px;height:583px;background:var(--panel)"></section>
<h2 class="heading" style="left:198px;top:2240px">Statement of<br>Oneness in Equity</h2>
<p class="copy" style="left:198px;top:2325px;width:358px">While division and separation define much of the current relationships on the planet, it is our cosmic destiny for all life to live in balance and harmony. Regardless of what may appear to separate us—such as nationality, language, ethnicity, race, class, sex, gender, political orientation, religion, or sexual orientation, to name a few—we are united in the most simple and profound ways. All life craves security, shelter, sustenance, love, and belonging. All life craves dignity and respect. At Serene Accord Education we design for our cosmic destiny. We are destined to be a planet where everyone (and all life form) belongs and no one is left out. With courage we release defensiveness and heal each other through the profound gift of listening. We acknowledge and stand witness to the harms done to wo/mankind, and with an unwavering commitment to healing and joy, we say enough.</p>
<div class="btn" style="left:198px;top:2574px;width:108px;height:39px">Read More</div>
<div class="photo" role="img" aria-label="Family running joyfully through a golden meadow at sunset" style="left:609px;top:2236px;width:411px;height:369px;background:linear-gradient(180deg,#f2c56a 0%,#e6a444 45%,#9c6a30 75%,#6a4a26 100%)"></div>

<!-- Testimonials -->
<section class="band testimonials" role="img" aria-label="Warm orange sunset over the sea"></section>
<h2 class="heading" style="left:0;width:1200px;top:2803px;text-align:center;color:var(--white);font-weight:400;font-size:30px">Client Testimonials</h2>
<div class="photo" role="img" aria-label="Client portrait" style="left:554px;top:2870px;width:90px;height:90px;border-radius:50%;border:3px solid var(--white);background:linear-gradient(180deg,#cfe0ea,#c89a6e)"></div>
<p class="quote">Lorem ipsum dolor sit amet, consectetur adipiscing elit, sed do eiusmod empor incididunt ut labore et dolore magna aliqua. Quis ipsum suspendisse ultrices gravidaisus commodo viverra maecenas accumsan lacus vel facilisis.</p>
<svg class="abs" style="left:268px;top:2993px" width="16" height="20" viewBox="0 0 16 20"><path d="M11 2 L4 10 L11 18" fill="none" stroke="#fff" stroke-width="2.5"/></svg>
<svg class="abs" style="left:918px;top:2993px" width="16" height="20" viewBox="0 0 16 20"><path d="M5 2 L12 10 L5 18" fill="none" stroke="#fff" stroke-width="2.5"/></svg>
<div class="abs" style="left:0;width:1200px;top:3063px;text-align:center;font-weight:700;font-size:18px;color:var(--white)">Quiet River</div>
<span class="dot" style="left:575px"></span><span class="dot" style="left:593px"></span><span class="dot" style="left:611px"></span>

<!-- Newsletter -->
<h2 class="heading" style="left:198px;top:3238px;font-size:23px;font-weight:400;letter-spacing:1.5px">Newsletter Signup</h2>
<div class="field" style="left:492px;width:190px">Name</div>
<div class="field" style="left:692px;width:189px">Email</div>
<div class="btn" style="left:892px;top:3232px;width:107px;height:40px">Sign Up</div>

<!-- Footer -->
<footer class="band footer"></footer>
<div class="seal" style="left:531px;top:3347px;width:136px;height:136px;font-size:14px;line-height:18px">Serene<br>Accord<br>Academy</div>
<nav class="nav" style="top:3512px">
  <span style="left:239px">Home</span><span style="left:309px">About</span><span style="left:420px">School Foundations</span><span style="left:549px">Curriculum</span><span style="left:646px">Pedagogy</span><span style="left:744px">Outcomes</span><span style="left:837px">Opening</span><span style="left:940px">Testimonials</span>
</nav>
<p class="abs" style="left:0;width:1200px;top:3553px;text-align:center;font-size:12.5px;color:var(--white)">Copyright © 2023 Serene Accord Academy. All Rights reserved.</p>

</body>
</html>
```